"Breathe & Bloom" Book Cover 5.5x8.5

Title of the book is "Breathe & Bloom"
Subtitle is "Unmasking Pricing Myths"
I've used PixelGuild on multiple occasions you can look on my Borvex page, Mark Delwitt, to see the covers I've used in the other projects I've done.
The target audience are people who have been tricked to think they can't retire because inflation, i.e. cost of living is going up so much they must work to keep up. There is no evidence of this.
And those are the people I want to reach so they can "Breathe...and Bloom."
Target Market(s)
Americans aged 55 and over who are thinking about retirement
Industry/Entity Type
Financial
Requirements
Nice to have
- Keep It Simple, Stupid is my mantra. Just make it pop out when people are browsing
Should not have
- No piggy banks. No old people sitting on a beach.

```html
<!DOCTYPE html>
<html lang="en">
<head>
<meta charset="utf-8">
<title>Breathe &amp; Bloom — Book Cover</title>
<link rel="stylesheet" href="https://fonts.googleapis.com/css2?family=Anton&family=Oswald:wght@500;700&display=swap">
<style>
  :root {
    --page-bg: #e6e6e6;
    --page-glow: #f6f6f6;
    --wood-light: #f2f1ef;
    --wood-mid: #d8d6d2;
    --leather-hi: #c8683e;
    --leather: #a8482a;
    --leather-dark: #6e2c16;
    --band: rgba(45, 45, 45, 0.9);
    --title-white: #ffffff;
    --title-shadow: #111111;
    --author-ink: #111111;
  }
  * { margin: 0; padding: 0; box-sizing: border-box; }
  html, body {
    width: 1199px;
    height: 1200px;
    overflow: hidden;
  }
  body {
    position: relative;
    background: radial-gradient(circle at 50% 50%, var(--page-glow) 0%, var(--page-bg) 75%);
  }
  .book-cover {
    position: absolute;
    left: 267px;
    top: 101px;
    width: 665px;
    height: 995px;
    overflow: hidden;
    background: linear-gradient(180deg, var(--wood-light) 0%, var(--wood-mid) 100%);
  }
  .cover-photo {
    position: absolute;
    left: 104px;
    top: 74px;
    width: 508px;
    height: 800px;
    border-radius: 46% 48% 44% 42% / 38% 40% 30% 32%;
    background: radial-gradient(ellipse 70% 60% at 62% 40%, var(--leather-hi) 0%, var(--leather) 45%, var(--leather-dark) 100%);
    box-shadow: 18px 22px 40px rgba(0, 0, 0, 0.25);
  }
  .subtitle-band {
    position: absolute;
    left: 0;
    top: 85px;
    width: 100%;
    height: 62px;
    background: var(--band);
    display: flex;
    align-items: center;
    justify-content: center;
  }
  .subtitle {
    font-family: "Oswald", sans-serif;
    font-weight: 500;
    font-size: 43px;
    letter-spacing: 1.5px;
    color: var(--title-white);
    text-transform: uppercase;
    line-height: 1;
  }
  .title {
    position: absolute;
    left: 0;
    top: 330px;
    width: 100%;
    text-align: center;
    font-family: "Anton", sans-serif;
    font-weight: 400;
    color: var(--title-white);
    text-transform: uppercase;
    text-shadow: 4px 4px 0 var(--title-shadow);
    line-height: 0.9;
    font-size: 124px;
  }
  .title-line, .title-amp { display: block; }
  .title-amp { margin-top: 14px; }
  .title-line + .title-amp + .title-line { margin-top: 26px; }
  .author {
    position: absolute;
    left: 0;
    bottom: 18px;
    width: 100%;
    text-align: center;
    font-family: "Oswald", sans-serif;
    font-weight: 700;
    font-size: 56px;
    letter-spacing: -1.5px;
    line-height: 1.2;
    color: var(--author-ink);
  }
</style>
</head>
<body>
  <main class="book-cover">
    <div class="cover-photo" role="img" aria-label="Photo of a pair of worn red leather boxing gloves hanging by their laces against white-painted wooden planks"></div>
    <div class="subtitle-band">
      <p class="subtitle">Unmasking Pricing Myths</p>
    </div>
    <h1 class="title">
      <span class="title-line">Breathe</span>
      <span class="title-amp">&amp;</span>
      <span class="title-line">Bloom</span>
    </h1>
    <p class="author">Mark Delwitt</p>
  </main>
</body>
</html>
```